Pregnancy and Fertility Information Website

Hello Designers,
I need a website which provide tips and information about healthy and happy pregnancy. My website name is Lorvin medical.

The website should provide all the information needed throughout pregnancy and beyond ranging from pregnancy tracking tools and articles about common pregnancy concerns and what to expect during pregnancy,etc.
The details about first trimester, second trimester and third trimester should be highlighted in the website.

Top Navigation
Home, Fertility, Pregnancy basics, Articles, Tips and News

I'm looking for a simple and clean design which involves captivating images and colors but it shouldn't be crowded. The design must be professional and modern. An easy to navigate layout is a must.

Green, violet, blue and light yellow colors are my favorites but i'm open to other options.

Any questions. Kindly ask

Industry/Entity Type

Medical

```html
<!DOCTYPE html>
<html lang="en">
<head>
<meta charset="utf-8">
<title>Lorvin medical – Healthy &amp; Happy Pregnancy</title>
<link href="https://fonts.googleapis.com/css2?family=Mulish:wght@300;400;600;700&display=swap" rel="stylesheet">
<style>
:root{
  --blue:#1d87d2;
  --blue-dark:#136bb0;
  --green:#5cb646;
  --green-grad:#4db649;
  --violet:#3a1f5d;
  --violet-footer:#3b2662;
  --yellow:#ffe100;
  --ink:#333338;
  --muted:#7a7a80;
  --line:#e3e3e6;
  --white:#ffffff;
}
*{box-sizing:border-box;margin:0;padding:0}
html,body{width:1200px;height:3333px;overflow:hidden}
body{font-family:"Mulish",sans-serif;color:var(--ink);background:var(--white);position:relative}
.abs{position:absolute}
a{color:inherit;text-decoration:none}

/* nav */
.site-nav{position:absolute;top:0;left:0;width:1200px;height:111px;background:var(--white);z-index:5}
.nav-link{position:absolute;top:50px;font-size:17px;color:#444}
.nav-link.active{color:var(--green)}
.nav-link.active::after{content:"";position:absolute;left:0;right:0;top:42px;height:3px;background:var(--green)}
.brand{position:absolute;left:515px;top:0;width:170px;height:150px;border-radius:0 0 85px 85px;background:var(--white);display:flex;align-items:center;justify-content:center;z-index:6}
.brand-name{font-size:22px;font-weight:700;color:var(--blue);text-align:center;line-height:1.1}

/* hero */
.hero{top:111px;left:0;width:1200px;height:527px;background:linear-gradient(90deg,#f5f3f1 0%,#f1ece7 45%,#e6d9cc 65%,#d9c5b2 78%,#efe8e2 100%)}
.hero-title{position:absolute;left:124px;top:140px;font-size:40px;font-weight:600;line-height:46px}
.hero-title .b{color:var(--blue)}
.hero-title .g{color:var(--green)}
.btn{position:absolute;display:flex;align-items:center;justify-content:center;color:var(--white);font-size:15px}
.btn-blue{background:linear-gradient(180deg,#2d97e0,var(--blue-dark))}
.btn-violet{background:linear-gradient(180deg,#4d2c78,var(--violet))}
.hero .btn{left:124px;top:302px;width:145px;height:38px}
.dots{position:absolute;left:122px;top:360px;display:flex;gap:6px}
.dots span{width:13px;height:13px;border-radius:50%;background:#cfcfcf}
.dots span:first-child{background:var(--white);border:2px solid #cfcfcf}

/* welcome */
.welcome{top:638px;left:0;width:1200px;height:426px;background:var(--white)}
.welcome-photo{position:absolute;left:644px;top:0;width:383px;height:426px;background:linear-gradient(180deg,#ece8e6 0%,#b9b6b6 40%,#8e8a8a 70%,#5c4f4a 100%)}
.welcome h2{position:absolute;left:124px;top:76px;font-size:34px;font-weight:300;color:#222}
.welcome p{position:absolute;left:124px;top:140px;width:470px;font-size:14.5px;line-height:22px;color:var(--muted)}
.welcome .btn{left:124px;top:324px;width:140px;height:38px}

/* steps */
.steps{top:1064px;left:0;width:1200px;height:540px;background:linear-gradient(105deg,#1589dc 0%,#1f9ac4 35%,#33aa8e 65%,var(--green-grad) 100%)}
.steps-title{position:absolute;top:42px;left:0;width:1200px;text-align:center;color:var(--white);font-size:27px;font-weight:300}
.steps-title::before,.steps-title::after{content:"";display:inline-block;width:38px;height:1px;background:rgba(255,255,255,.7);vertical-align:middle;margin:0 12px}
.trimester{position:absolute;top:114px;width:305px;height:322px;border:2px solid rgba(255,255,255,.45);color:var(--white);text-align:center}
.trimester svg{position:absolute;left:102px;top:24px}
.trimester h3{position:absolute;top:170px;left:0;right:0;font-size:24px;font-weight:400}
.trimester p{position:absolute;top:206px;left:34px;right:34px;font-size:12.5px;line-height:19px;opacity:.85}
.trimester .more{position:absolute;top:276px;left:0;right:0;font-size:14px;font-weight:700}
.steps-curve{position:absolute;left:0;bottom:0}

/* tips */
.tips-title{top:1586px;left:0;width:1200px;text-align:center;font-size:30px;font-weight:400;color:var(--blue)}
.tip{position:absolute;top:1644px;width:227px}
.tip-photo{width:227px;height:151px}
.tip h4,.article h4{font-size:15px;font-weight:700;color:#252538;margin-top:16px}
.tip p,.article p{font-size:12px;line-height:16px;color:var(--muted);margin-top:6px}
.read-more{display:block;font-size:11px;font-weight:700;color:var(--blue);margin-top:6px}
.divider{top:2007px;left:0;width:1200px;height:2px;background:var(--line)}

/* basics */
.basics{top:2009px;left:0;width:1200px;height:458px;background:linear-gradient(90deg,#f6f4f2 0%,#f7f7f8 60%,#f2f2f4 100%)}
.basics-photo{position:absolute;left:0;top:0;width:640px;height:458px;background:linear-gradient(120deg,#c58a55 0%,#e9cdb3 30%,#f4ebe4 55%,#f6f4f2 100%)}
.basics h2{position:absolute;left:647px;top:75px;font-size:30px;font-weight:400;color:var(--blue)}
.basics p{position:absolute;left:647px;top:125px;width:430px;font-size:14px;line-height:21px;color:var(--muted)}
.basics ul{position:absolute;left:647px;top:193px;list-style:none}
.basics li{font-size:14px;color:#555;height:31px;padding-left:22px;position:relative}
.basics li::before{content:"";position:absolute;left:2px;top:5px;border-left:7px solid var(--blue);border-top:4px solid transparent;border-bottom:4px solid transparent}
.basics .btn{left:647px;top:342px;width:148px;height:38px}

/* articles */
.articles{top:2467px;left:0;width:1200px;height:495px;background:var(--yellow)}
.articles h2{position:absolute;left:117px;top:52px;font-size:28px;font-weight:400;color:#1a1a1a}
.arrows{position:absolute;left:1032px;top:56px}
.article{position:absolute;top:106px;width:305px;height:316px;background:var(--white)}
.article-photo{height:174px}
.article-body{padding:14px 31px}
.article h4{margin-top:10px}

/* footer */
.site-footer{top:2962px;left:0;width:1200px;height:371px;background:var(--violet-footer);color:var(--white)}
.footer-brand{position:absolute;left:128px;top:110px;width:210px;display:flex;align-items:center;gap:12px;font-size:26px;font-weight:700}
.footer-brand i{width:22px;height:22px;border-radius:50%;background:var(--white);display:block}
.footer-col{position:absolute;top:62px}
.footer-col h5{font-size:16px;font-weight:400;letter-spacing:.5px;margin-bottom:14px}
.footer-col li{list-style:none;font-size:13px;line-height:30.5px;opacity:.9}
.social{display:flex;gap:6px;margin-top:12px}
.social span{width:30px;height:30px;border:2px solid var(--white);border-radius:50%}
.footer-rule{position:absolute;top:311px;left:103px;width:966px;height:1px;background:rgba(255,255,255,.25)}
.copyright{position:absolute;top:336px;left:0;width:1200px;text-align:center;font-size:11px;opacity:.7}
</style>
</head>
<body>

<header class="site-nav">
  <a class="nav-link active" style="left:147px">Home</a>
  <a class="nav-link" style="left:227px">Fertility</a>
  <a class="nav-link" style="left:316px">Pregnancy basics</a>
  <div class="brand"><span class="brand-name">Lorvin<br>medical</span></div>
  <a class="nav-link" style="left:731px">Articles</a>
  <a class="nav-link" style="left:827px">Tips and News</a>
  <a class="nav-link" style="left:976px">Contact us</a>
</header>

<section class="hero abs" role="img" aria-label="Smiling pregnant woman in a white top and beige cardigan holding her belly on a bright bed">
  <h1 class="hero-title"><span class="b">Tips and Information</span><br><span class="b">About Healthy &amp;</span><br><span class="g">Happy Pregnancy</span></h1>
  <a class="btn btn-blue">View Tips</a>
  <div class="dots"><span></span><span></span><span></span><span></span></div>
</section>

<section class="welcome abs">
  <h2>Welcome to Lorvin Medical</h2>
  <p>Ateger congue augue et malesuada iaculis ipsum dui aliquet felis at cursus magna nisl nec elit Praesent elementum elit at tellus nec ultricies sit amet porttitor mattis enim<br>In massa libero interdum nec interdum vel blandit sed nulla In ullamcorper est eget tempor cursus mi consectetuer mi a ltricies massa est sed nisl Class aptent taciti sociosqu</p>
  <a class="btn btn-violet">Learn More</a>
  <div class="welcome-photo" role="img" aria-label="Close view of a pregnant belly in a grey top, hands resting on it"></div>
</section>

<section class="steps abs">
  <h2 class="steps-title">Pregnancy Step by Step</h2>

  <article class="trimester" style="left:115px">
    <svg width="100" height="100" viewBox="0 0 100 100" fill="none" stroke="#fff" stroke-width="2.5"><circle cx="50" cy="50" r="40" stroke-opacity=".3" stroke-dasharray="2 5"/><rect x="40" y="24" width="18" height="48" rx="9" transform="rotate(40 50 50)"/><line x1="44" y1="44" x2="56" y2="56"/></svg>
    <h3>1st Trimester</h3>
    <p>Integer congue augue et malesuada iaculis ipsum dui aliquet felis at cursus magna nisl nec elit Praesent</p>
    <a class="more">Learn More &#8594;</a>
  </article>

  <article class="trimester" style="left:440px">
    <svg width="100" height="100" viewBox="0 0 100 100" fill="none" stroke="#fff" stroke-width="2.5"><circle cx="50" cy="50" r="40" stroke-opacity=".3" stroke-dasharray="2 5"/><circle cx="50" cy="50" r="20"/><circle cx="50" cy="50" r="6"/></svg>
    <h3>2nd Trimester</h3>
    <p>Integer congue augue et malesuada iaculis ipsum dui aliquet felis at cursus magna nisl nec elit Praesent</p>
    <a class="more">Learn More &#8594;</a>
  </article>

  <article class="trimester" style="left:767px">
    <svg width="100" height="100" viewBox="0 0 100 100" fill="none" stroke="#fff" stroke-width="2.5"><circle cx="50" cy="50" r="40" stroke-opacity=".3" stroke-dasharray="2 5"/><circle cx="50" cy="50" r="24"/><circle cx="50" cy="50" r="12"/></svg>
    <h3>3rd Trimester</h3>
    <p>Integer congue augue et malesuada iaculis ipsum dui aliquet felis at cursus magna nisl nec elit Praesent</p>
    <a class="more">Learn More &#8594;</a>
  </article>

  <svg class="steps-curve" width="1200" height="70" viewBox="0 0 1200 70" preserveAspectRatio="none"><path d="M0 70 C300 5 900 5 1200 60 L1200 70 Z" fill="#fff"/></svg>
</section>

<h2 class="tips-title abs">Tips and News</h2>

<article class="tip" style="left:122px">
  <div class="tip-photo" role="img" aria-label="Pregnant woman talking with a doctor" style="background:linear-gradient(120deg,#d9c4b6,#eef0f3)"></div>
  <h4>Your Tips Tittle here</h4>
  <p>Integer congue augue et malesuada iaculis ipsum dui aliquet felis at cursus magna nisl nec elit Praesent elementum elit at tellus nec</p>
  <a class="read-more">READ MORE</a>
</article>
<article class="tip" style="left:367px">
  <div class="tip-photo" role="img" aria-label="Hands holding a pregnancy test" style="background:linear-gradient(120deg,#eef0f3,#d8cfc6)"></div>
  <h4>Your Tips Tittle here</h4>
  <p>Integer congue augue et malesuada iaculis ipsum dui aliquet felis at cursus magna nisl nec elit Praesent elementum elit at tellus nec</p>
  <a class="read-more">READ MORE</a>
</article>
<article class="tip" style="left:613px">
  <div class="tip-photo" role="img" aria-label="Pregnant woman eating a fresh salad" style="background:linear-gradient(120deg,#e6dcd2,#b9c98f)"></div>
  <h4>Your Tips Tittle here</h4>
  <p>Integer congue augue et malesuada iaculis ipsum dui aliquet felis at cursus magna nisl nec elit Praesent elementum elit at tellus nec</p>
  <a class="read-more">READ MORE</a>
</article>
<article class="tip" style="left:858px">
  <div class="tip-photo" role="img" aria-label="Pregnant woman doing yoga in a purple top" style="background:linear-gradient(120deg,#e9e2e8,#c58fc7)"></div>
  <h4>Your Tips Tittle here</h4>
  <p>Integer congue augue et malesuada iaculis ipsum dui aliquet felis at cursus magna nisl nec elit Praesent elementum elit at tellus nec</p>
  <a class="read-more">READ MORE</a>
</article>

<div class="divider abs"></div>

<section class="basics abs">
  <div class="basics-photo" role="img" aria-label="Mother holding and kissing her newborn baby"></div>
  <h2>Pregnancy Basics</h2>
  <p>Donec dictum lectus non odio Cras a ante vitae enim iaculis aliquam Mauris nunc quam venenatis</p>
  <ul>
    <li>Aec euismod sit amet egestas</li>
    <li>Placerat est Pellentesque habitant morbi</li>
    <li>Tristique senectus et netus</li>
    <li>Et malesuada fames ac turpis egestas</li>
  </ul>
  <a class="btn btn-blue">Learn More</a>
</section>

<section class="articles abs">
  <h2>Latest Articles</h2>
  <svg class="arrows" width="50" height="24" viewBox="0 0 50 24" fill="none" stroke="#1a1a1a" stroke-width="2.5"><path d="M12 3 L4 12 L12 21"/><path d="M38 3 L46 12 L38 21"/></svg>

  <article class="article" style="left:115px">
    <div class="article-photo" role="img" aria-label="Pregnant woman resting on a white bed" style="background:linear-gradient(120deg,#eee9e4,#c9a48a)"></div>
    <div class="article-body">
      <h4>Article Tittle here</h4>
      <p>Integer congue augue et malesuada iaculis ipsum dui aliquet felis at cursus magna nisl nec elit Praesent</p>
      <a class="read-more">READ MORE</a>
    </div>
  </article>
  <article class="article" style="left:447px">
    <div class="article-photo" role="img" aria-label="Pregnant woman sitting beside a bowl of fresh fruit" style="background:linear-gradient(120deg,#dcd6d0,#e7b57a)"></div>
    <div class="article-body">
      <h4>Article Tittle here</h4>
      <p>Integer congue augue et malesuada iaculis ipsum dui aliquet felis at cursus magna nisl nec elit Praesent</p>
      <a class="read-more">READ MORE</a>
    </div>
  </article>
  <article class="article" style="left:775px">
    <div class="article-photo" role="img" aria-label="Pregnant woman exercising with pink dumbbells" style="background:linear-gradient(120deg,#e8e4e6,#d68aa8)"></div>
    <div class="article-body">
      <h4>Article Tittle here</h4>
      <p>Integer congue augue et malesuada iaculis ipsum dui aliquet felis at cursus magna nisl nec elit Praesent</p>
      <a class="read-more">READ MORE</a>
    </div>
  </article>
</section>

<footer class="site-footer abs">
  <div class="footer-brand"><i></i>Lorvin medical</div>
  <div class="footer-col" style="left:438px">
    <h5>ABOUT US</h5>
    <ul><li>What We Do</li><li>Pregnancy basics</li><li>Articles</li><li>News &amp; Tips</li></ul>
  </div>
  <div class="footer-col" style="left:636px">
    <h5>RESOURCES</h5>
    <ul><li>Videos</li><li>Blogs</li><li>Fertility</li><li>Contact</li></ul>
  </div>
  <div class="footer-col" style="left:847px">
    <h5>CONTACT US</h5>
    <ul><li>48 Willow Bend Road Suite 12</li><li>Brookvale, ST 10482</li><li>1-800-555-0142</li><li>hello@lorvinmedical.example</li></ul>
    <div class="social"><span></span><span></span><span></span><span></span></div>
  </div>
  <div class="footer-rule"></div>
  <p class="copyright">© 2017 Company Name &nbsp;All right reserved &nbsp;Term of Use</p>
</footer>

</body>
</html>
```